Stationery Design Project

I am looking for stationary design for an automotive collision repair company. This needs to work with my business cards just designed here. I've attached. I need 8.5 x 11 stationary and corissponding envelopes. a post it note pad also. Our companies focus is very high end customer service driven . Our customer base is 35-65 middle to high income. Please include company name, logo, address, phone number, web address. The business card is two greys with green and white writing. I invision a light grey background with a darker grey band on it that contains the logo.

I justĀ 

Why is no one touching this project

Target Market(s)

60%. Women 40% men. Age 35-60

Industry/Entity Type

Automotive

Requirements
Must have
• Tie in with business cards. So it needs grey tones with green and white logo. Name, address, phone and web address. Must have 8.5 x 11 paper and envelopes.
Nice to have
• Post it notes

```html
<!DOCTYPE html>
<html lang="en">
<head>
<meta charset="utf-8">
<title>PanelCraft Stationery</title>
<link rel="stylesheet" href="https://fonts.googleapis.com/css2?family=Oswald:wght@600&family=Arimo:wght@400&family=Pinyon+Script&display=swap">
<style>
  :root {
    --backdrop: #e2e2e2;
    --paper: #fbfbfb;
    --charcoal: #3d3c3d;
    --green: #8bbd2b;
    --green-soft: #cfe49a;
    --ink: #444444;
    --footer-ink: #d8d8d8;
  }
  * { box-sizing: border-box; margin: 0; padding: 0; }
  html, body { width: 1200px; height: 851px; overflow: hidden; }
  body {
    background: var(--backdrop);
    position: relative;
    font-family: "Arimo", Arial, sans-serif;
  }
  .sheet {
    position: absolute;
    background: var(--paper);
    overflow: hidden;
  }
  .sheet > svg.bands {
    position: absolute; inset: 0; width: 100%; height: 100%;
  }
  .brand-name {
    position: absolute;
    font-family: "Oswald", "Arial Narrow", sans-serif;
    font-weight: 600;
    color: var(--green);
    letter-spacing: 0.2px;
    line-height: 1;
    white-space: nowrap;
  }
  .contact {
    position: absolute;
    display: flex;
    align-items: flex-start;
    line-height: 1.45;
  }
  .contact .col { padding: 0 8px; border-left: 1px solid currentColor; }
  .contact .col:first-child { padding-left: 0; border-left: none; }
  .contact .tag { color: var(--green); margin-right: 4px; }

  /* Letterhead */
  .letterhead { left: 105px; top: 80px; width: 385px; height: 588px; }
  .letterhead .brand-name { top: 72px; left: 0; width: 100%; text-align: center; font-size: 22px; }
  .letterhead .contact { top: 565px; left: 98px; font-size: 5.5px; color: var(--footer-ink); }
  .letterhead .contact .col { border-color: #6a6a6a; }

  /* Compliments slip / envelope */
  .envelope { left: 590px; top: 128px; width: 526px; height: 267px; }
  .envelope .brand-name { top: 38px; left: 0; width: 270px; text-align: center; font-size: 24px; }
  .envelope .contact { top: 230px; left: 19px; font-size: 7px; color: var(--ink); }
  .envelope .contact .col { border-color: #b5b5b5; }
  .envelope .compliments {
    position: absolute; top: 206px; left: 260px;
    font-family: "Pinyon Script", cursive;
    font-size: 40px; line-height: 1; color: var(--charcoal); white-space: nowrap;
  }
  .envelope .compliments .lead { color: var(--green); margin-right: 10px; }

  /* Sticky note pad */
  .sticky-note { left: 737px; top: 490px; width: 243px; height: 238px; }
  .sticky-note .brand-name { top: 217px; left: 21px; font-size: 15px; }
</style>
</head>
<body>

  <section class="sheet letterhead" aria-label="Letterhead">
    <svg class="bands" viewBox="0 0 385 588" preserveAspectRatio="none" aria-hidden="true">
      <path d="M0 0H385V108C300 96 250 112 190 121C120 131 60 126 0 130Z" fill="var(--charcoal)"/>
      <path d="M0 136C60 132 120 137 190 127C250 118 300 102 385 113" fill="none" stroke="var(--green-soft)" stroke-width="5"/>
      <path d="M0 131C60 127 120 132 190 122C250 113 300 97 385 108" fill="none" stroke="var(--green)" stroke-width="2.5"/>
      <path d="M0 588V556C80 547 150 541 220 545C300 550 350 549 385 541V588Z" fill="var(--charcoal)"/>
      <path d="M0 550C80 541 150 535 220 539C300 544 350 543 385 535" fill="none" stroke="var(--green-soft)" stroke-width="5"/>
      <path d="M0 555C80 546 150 540 220 544C300 549 350 548 385 540" fill="none" stroke="var(--green)" stroke-width="2.5"/>
    </svg>
    <div class="brand-name">PanelCraft</div>
    <div class="contact">
      <div class="col">218 Panel Lane<br>Brookfield 3120</div>
      <div class="col"><span class="tag">t.</span>03 5550 1234<br><span class="tag">f.</span>03 5550 5678</div>
      <div class="col">www.panelcraftauto.com<br>mia@panelcraftauto.com</div>
    </div>
  </section>

  <section class="sheet envelope" aria-label="Envelope">
    <svg class="bands" viewBox="0 0 526 267" preserveAspectRatio="none" aria-hidden="true">
      <path d="M0 0H526V74C430 80 340 88 250 90C150 92 70 92 0 100Z" fill="var(--charcoal)"/>
      <path d="M0 108C70 100 150 100 250 97C340 95 430 87 526 82" fill="none" stroke="var(--green-soft)" stroke-width="5"/>
      <path d="M0 103C70 95 150 95 250 92C340 90 430 82 526 77" fill="none" stroke="var(--green)" stroke-width="2.5"/>
    </svg>
    <div class="brand-name">PanelCraft</div>
    <div class="contact">
      <div class="col">218 Panel Lane<br>Brookfield 3120</div>
      <div class="col"><span class="tag">t.</span>03 5550 1234<br><span class="tag">f.</span>03 5550 5678</div>
      <div class="col">www.panelcraftauto.com<br>mia@panelcraftauto.com</div>
    </div>
    <div class="compliments"><span class="lead">With</span>Compliments</div>
  </section>

  <section class="sheet sticky-note" aria-label="Sticky note pad">
    <svg class="bands" viewBox="0 0 243 238" preserveAspectRatio="none" aria-hidden="true">
      <path d="M0 238V210C50 206 110 206 160 196C200 190 225 192 243 198V238Z" fill="var(--charcoal)"/>
      <path d="M0 206C50 202 110 202 160 193C200 186 225 188 243 194" fill="none" stroke="var(--green-soft)" stroke-width="4"/>
      <path d="M0 209C50 205 110 205 160 196C200 189 225 191 243 197" fill="none" stroke="var(--green)" stroke-width="2"/>
    </svg>
    <div class="brand-name">PanelCraft</div>
  </section>

</body>
</html>
```